Business card design needed

We are a start up Mobile Vet Clinic.
We will be servicing an are that cover the Gladstone Region Shire.
Bookings will be made via the number listed or email address.
Travel will be charged

Target Market(s)

Pet Owners

Industry/Entity Type

Business

Contact Information for Business Card

BRINDELLA MOBILE VET
Tarrowen Pty Ltd
Dana Fosterby BVSc
27 Wexhaven St
Marrindale VIC 3999

PH: 0743186209 Fax: 0743186514 email: bmvet@quillnet.example

Logo styles of interest
Pictorial/Combination Logo

```html
<!DOCTYPE html>
<html lang="en">
<head>
<meta charset="utf-8">
<title>Brindella Mobile Vet – Business Card</title>
<link rel="stylesheet" href="https://fonts.googleapis.com/css2?family=Tenor+Sans&family=Open+Sans:wght@400&display=swap">
<style>
  :root {
    --paper: #ffffff;
    --brand-blue: #2aa6dd;
    --art-light: #e6f5fc;
    --art-mid: #cdeaf8;
    --band-top: #1f95d4;
    --band-bottom: #5cc2ee;
    --band-text: #ffffff;
  }
  * { margin: 0; padding: 0; box-sizing: border-box; }
  html, body {
    width: 1200px;
    height: 667px;
    overflow: hidden;
    background: var(--paper);
  }
  .card {
    position: relative;
    width: 1200px;
    height: 667px;
    background: var(--paper);
  }
  .brand-art {
    position: absolute;
    left: 340px;
    top: 55px;
    width: 560px;
    height: 212px;
    border-radius: 8px;
    background: linear-gradient(180deg, var(--art-light), var(--art-mid));
  }
  .brand-name {
    position: absolute;
    left: 0;
    right: 0;
    top: 310px;
    text-align: center;
    font-family: "Tenor Sans", sans-serif;
    font-weight: 400;
    font-size: 80px;
    letter-spacing: 0;
    line-height: 1;
    white-space: nowrap;
    color: var(--brand-blue);
  }
  .contact-band {
    position: absolute;
    left: 0;
    top: 421px;
    width: 1200px;
    height: 246px;
    background: linear-gradient(180deg, var(--band-top), var(--band-bottom));
    display: flex;
    flex-direction: column;
    align-items: center;
    justify-content: center;
    padding-bottom: 24px;
  }
  .contact-line {
    font-family: "Open Sans", sans-serif;
    font-size: 34px;
    line-height: 50px;
    letter-spacing: 1px;
    color: var(--band-text);
    text-align: center;
    white-space: nowrap;
  }
</style>
</head>
<body>
  <main class="card">
    <div class="brand-art" role="img" aria-label="Line illustration of a dog and a cat beside a medical cross"></div>
    <h1 class="brand-name">BRINDELLA MOBILE VET</h1>
    <section class="contact-band">
      <p class="contact-line">Tarrowen Pty Ltd Dana Fosterby BVSc</p>
      <p class="contact-line">27 Wexhaven St Marrindale; VIC 3999 PH: 0743186209</p>
      <p class="contact-line">Fax: 0743186514; email: bmvet@quillnet.example</p>
    </section>
  </main>
</body>
</html>
```